VORLEN Website Design

We need a website designed for our company VORLEN. We are a luxury lifestyle club that will provide benefits and services for our members. The site should be clean & sleek, preferably using black and white (or darker colors). (example sites: brimvale.example, tusko.example)

Here is a link of a sample page I did using wix. (https://pelmundry4.sitebuild.example/mypage) This can be used to get a general idea.

Target Market(s)

Upper Middle Class in the United States

Number of Pages Required

5+ page

Font styles to use
Sans Serif
Other font styles liked:
• Arial (or other similar fonts)

Requirements
Must have
• A clean design that is eye-catching and speaks to our company.
Nice to have
• Ideas for copy.

```html
<!DOCTYPE html>
<html lang="en">
<head>
<meta charset="utf-8">
<title>VORLEN — Memberships</title>
<link rel="stylesheet" href="https://fonts.googleapis.com/css2?family=Montserrat:wght@400;500;600;700&display=swap">
<style>
  :root {
    --bg: #1c1c1e;
    --hero-dark: #141416;
    --hero-mid: #2a2628;
    --hero-warm: #4a3a30;
    --band: #232325;
    --text: #ffffff;
    --muted: #cfcfd4;
    --accent: #3b6cf0;
  }
  * { box-sizing: border-box; margin: 0; padding: 0; }
  html, body { width: 1200px; height: 800px; overflow: hidden; background: var(--bg); }
  body { font-family: "Montserrat", Arial, sans-serif; color: var(--text); position: relative; }

  .hero { position: absolute; left: 0; top: 0; width: 1200px; height: 600px; }
  .hero-photo {
    position: absolute; inset: 0;
    background:
      radial-gradient(ellipse 60% 55% at 55% 45%, rgba(120,70,60,0.45), transparent 70%),
      linear-gradient(180deg, var(--hero-mid) 0%, var(--hero-dark) 55%, var(--hero-warm) 100%);
  }
  .hero-shade { position: absolute; inset: 0; background: rgba(10,10,12,0.45); }

  .site-header {
    position: absolute; left: 0; top: 0; width: 100%; height: 110px;
    display: flex; align-items: center; justify-content: space-between;
    padding: 0 70px 0 110px;
  }
  .brand { display: flex; align-items: center; gap: 12px; }
  .brand-mark { width: 14px; height: 14px; background: var(--text); }
  .brand-name { font-size: 34px; font-weight: 500; letter-spacing: 1px; color: var(--text); }

  .main-nav { display: flex; align-items: center; gap: 28px; font-size: 13px; font-weight: 500; }
  .main-nav a { color: var(--text); text-decoration: none; }
  .main-nav a.is-active { border-bottom: 2px solid var(--text); padding-bottom: 3px; }
  .search-btn {
    width: 26px; height: 26px; border-radius: 50%; background: var(--accent);
    display: flex; align-items: center; justify-content: center;
  }

  .hero-title {
    position: absolute; left: 110px; top: 240px; width: 960px;
    font-size: 44px; font-weight: 600; line-height: 1.35; text-transform: uppercase;
    letter-spacing: 0.5px;
  }
  .slide-arrow { position: absolute; top: 270px; width: 24px; height: 40px; }
  .slide-arrow.prev { left: 40px; }
  .slide-arrow.next { right: 40px; top: 340px; }

  .slide-dots { position: absolute; left: 50%; top: 560px; transform: translateX(-50%); display: flex; gap: 6px; }
  .slide-dots span { width: 8px; height: 8px; border-radius: 50%; background: var(--muted); }
  .slide-dots span.is-current { background: var(--accent); }

  .about-band { position: absolute; left: 0; top: 600px; width: 1200px; height: 200px; background: var(--band); }
  .about-toggle { position: absolute; left: 50%; top: -30px; transform: translateX(-50%); }
  .about-title {
    position: absolute; left: 0; width: 100%; top: 40px; text-align: center;
    font-size: 32px; font-weight: 500; letter-spacing: 1px;
  }
</style>
</head>
<body>
  <section class="hero">
    <div class="hero-photo" role="img" aria-label="Photo of performers holding hands and bowing on a stage"></div>
    <div class="hero-shade"></div>

    <header class="site-header">
      <div class="brand">
        <span class="brand-mark"></span>
        <span class="brand-name">VORLEN</span>
      </div>
      <nav class="main-nav">
        <a href="#" class="is-active">Home</a>
        <a href="#">About us</a>
        <a href="#">Services &amp; Benefits</a>
        <a href="#">Contact</a>
        <span class="search-btn">
          <svg width="12" height="12" viewBox="0 0 12 12"><circle cx="5" cy="5" r="3.5" fill="none" stroke="#fff" stroke-width="1.6"/><line x1="7.6" y1="7.6" x2="11" y2="11" stroke="#fff" stroke-width="1.6"/></svg>
        </span>
      </nav>
    </header>

    <svg class="slide-arrow prev" viewBox="0 0 24 40"><polyline points="18,8 6,20 18,32" fill="none" stroke="#fff" stroke-width="3"/></svg>
    <h1 class="hero-title">Memberships for creatives, athletes, artists, and other professionals.</h1>
    <svg class="slide-arrow next" viewBox="0 0 24 40"><polyline points="6,8 18,20 6,32" fill="none" stroke="#fff" stroke-width="3"/></svg>

    <div class="slide-dots"><span class="is-current"></span><span></span><span></span></div>
  </section>

  <section class="about-band">
    <svg class="about-toggle" width="60" height="30" viewBox="0 0 60 30">
      <polygon points="30,0 60,30 0,30" fill="var(--accent)"/>
      <polyline points="24,17 30,22 36,17" fill="none" stroke="#fff" stroke-width="2"/>
    </svg>
    <h2 class="about-title">ABOUT US</h2>
  </section>
</body>
</html>
```